Ridgeline Throttle Touring Company needs brochure

We need a brochure for our motorcycle tour company, we run tours and provide other services like day rides, bespoke trips, heli taxis, trekking, mountain biking, white water rafting etc. We are a small company that runs the tours ourselves, providing excellent customer service . We are team of international friendly motorcycle enthusiasts with a passion for Nepal. With an office in the UK and in Nepal. Our brochure should reflect quality adventures, showcasing the Nepal Himalayas, our tours, and shout adventure. Target audience are Adventure Bikers. Below are some photos (all of which are owned by us, for use on our brochure only) Also the document with all the content for the brochure.

Target Market(s)

Adventure Motorbike Riders

Industry/Entity Type

Travel

Other font styles liked:
• Aurora for headings...

Requirements
Must have
• Adventure Feel. Looking cool and modern. Well thought out colour palette. Include big photos. Sometimes as background to text.
• touring in the himalayas:
Nice to have
• Infographics for the include exclude section.
• Want it to be A5 brochure, landscape, probably be needing 14 pages. Might make it shorter to 12 if possible.
• If you have access to vectors/graphics please use stuff related to Nepal like Buddhas eyes, stupas, prayer flags, bells, shiva trident, mountains, tyre tracks etc. Be imaginative and creative. I have uploaded a photo of rough layout but is quite open to interpretation. Need photos and text to be clear. Please let me know if any photos are not good quality.
Should not have
• It shouldn't look like a corporate brochure, boring,
• It shouldn't look like a Brokker Vantell type trip. We use adventure bikes.

```html
<!DOCTYPE html>
<html lang="en">
<head>
<meta charset="utf-8">
<title>Ridgeline Throttle Touring Company – Brochure Spreads</title>
<link href="https://fonts.googleapis.com/css2?family=Oswald:wght@500;700&family=Montserrat:wght@600;700;800&family=Open+Sans:wght@400;600&display=swap" rel="stylesheet">
<style>
  :root{
    --bg:#e5e5e7;
    --paper:#f4f4f6;
    --red:#c8202c;
    --deep-red:#6e0e16;
    --orange:#e0583a;
    --navy:#2b2f86;
    --navy-deep:#1d2060;
    --grey:#8a8b8f;
    --ink:#2a2a2e;
    --white:#ffffff;
  }
  *{box-sizing:border-box;margin:0;padding:0}
  html,body{width:1200px;height:2236px;overflow:hidden;background:var(--bg)}
  body{position:relative;font-family:"Open Sans",Arial,sans-serif;color:var(--ink)}
  .spread{position:absolute;left:60px;width:1080px;height:620px;overflow:hidden;background:var(--paper);box-shadow:0 6px 18px rgba(0,0,0,.12)}
  .spread--outer{top:94px}
  .spread--inside{top:808px}
  .spread--services{top:1522px}
  .panel{position:absolute;top:0;height:100%;overflow:hidden}
  .photo{position:absolute;display:block}
  .brand{position:absolute;display:flex;align-items:center;gap:8px;font-family:"Montserrat",Arial,sans-serif;font-weight:800;font-size:15px;color:var(--red);letter-spacing:.5px;text-transform:uppercase}
  .brand__dot{width:20px;height:20px;border-radius:50%;background:var(--red)}
  .web{font-family:"Oswald",Arial,sans-serif;font-weight:700;letter-spacing:1px}
  .body-text{font-size:10.5px;line-height:1.55}
  .body-text p{margin-bottom:8px}
  .heading{font-family:"Montserrat",Arial,sans-serif;font-weight:800;font-size:19px;position:relative;padding-bottom:8px;margin-bottom:12px}
  .heading::after{content:"";position:absolute;left:0;bottom:0;width:56px;height:3px;background:var(--red)}
  .heading--light{color:var(--white)}
  .heading--navy{color:var(--navy)}

  /* outer spread */
  .back-panel{left:0;width:360px;background:var(--paper)}
  .back-panel .brand{top:40px;left:34px}
  .back-panel .rider-photo{left:70px;top:100px;width:220px;height:160px;background:linear-gradient(160deg,#5b6b3e,#2d3322 60%,#7a6e55);border:6px solid var(--ink)}
  .back-panel .sq-orange{position:absolute;left:120px;top:290px;width:44px;height:44px;background:var(--orange)}
  .back-panel .sq-navy{position:absolute;left:176px;top:322px;width:60px;height:60px;background:var(--navy)}
  .back-panel .web{position:absolute;left:300px;top:590px;transform:rotate(-90deg);transform-origin:left top;font-size:22px;color:var(--white);white-space:nowrap}
  .contact-panel{left:360px;width:360px;color:var(--white)}
  .contact-panel .texture{inset:0;width:100%;height:100%;background:linear-gradient(170deg,#b5141f,#8e0f18 55%,#c8202c)}
  .contact-panel__inner{position:absolute;inset:34px 30px;text-align:center}
  .contact-panel h3{font-family:"Montserrat",Arial,sans-serif;font-weight:800;font-size:17px;margin-bottom:8px}
  .contact-panel .map{position:relative;margin:12px auto;width:120px;height:120px;border-radius:50%;background:radial-gradient(circle,#d8d8da,#9a9a9e)}
  .contact-panel .lead{font-family:"Montserrat",Arial,sans-serif;font-weight:700;font-size:13px;margin:10px 0 4px}
  .contact-panel .detail{font-family:"Montserrat",Arial,sans-serif;font-weight:700;font-size:12px;line-height:1.6}
  .contact-panel small{display:block;font-size:9.5px;line-height:1.5;margin-top:10px;opacity:.92}
  .cover-panel{left:720px;width:360px;background:var(--paper)}
  .cover-panel .mountain-photo{left:0;top:0;width:360px;height:380px;background:linear-gradient(180deg,#b9c7da 0%,#eef1f5 28%,#8d7a66 55%,#5d4a3a 100%)}
  .cover-panel .brand{top:28px;left:24px;color:var(--white)}
  .cover-panel .brand__dot{background:var(--white)}
  .cover-panel__title{position:absolute;right:28px;top:404px;width:200px;font-family:"Oswald",Arial,sans-serif;font-weight:700;font-size:30px;line-height:1.05;color:var(--red);text-transform:uppercase;text-align:right}
  .cover-panel__url{position:absolute;left:110px;right:0;bottom:44px;height:36px;background:var(--grey);color:var(--white);font-size:17px;line-height:36px;padding-left:18px}

  /* inside spread */
  .about-page{left:0;width:540px;color:var(--white)}
  .about-page .road-photo{inset:0;width:100%;height:100%;background:linear-gradient(165deg,#3a0a0e 0%,#7d1019 45%,#c8202c 80%,#5c0d12 100%)}
  .about-page__col{position:absolute;top:40px;width:232px}
  .about-page__col--a{left:34px}
  .about-page__col--b{left:286px;top:40px}
  .about-page .heading{margin-top:4px}
  .about-page .heading + .body-text{margin-bottom:14px}
  .touring-page{left:540px;width:540px;background:var(--paper)}
  .touring-page__inner{position:absolute;left:36px;right:36px;top:44px}
  .touring-page .heading{font-size:21px}
  .touring-page .heading::after{left:auto;right:0}
  .touring-page .heading{text-align:right}
  .page-band{position:absolute;left:0;right:0;bottom:0;height:26px}

  /* services spread */
  .story-page{left:0;width:540px;color:#e6e7f5}
  .story-page .valley-photo{inset:0;width:100%;height:100%;background:linear-gradient(160deg,#2b2f86 0%,#23276f 50%,#3e4394 100%)}
  .story-page__col{position:absolute;top:46px;width:222px}
  .story-page__col--a{left:36px}
  .story-page__col--b{left:284px}
  .services-page{left:540px;width:540px;background:var(--paper)}
  .services-page__inner{position:absolute;left:40px;top:60px;width:280px}
  .services-list{list-style:none;font-size:10.5px;line-height:1.5}
  .services-list li{margin-bottom:7px}
  .services-list strong{color:var(--navy)}
  .partner{margin-top:20px;font-size:10px;font-style:italic;color:var(--grey)}
  .partner-badge{margin-top:8px;width:110px;height:44px;background:#d9d9dc}
  .collage{position:absolute}
</style>
</head>
<body>

<!-- Outer spread: back, contact, cover -->
<section class="spread spread--outer">
  <div class="panel back-panel">
    <div class="brand"><span class="brand__dot"></span>Ridgeline Throttle</div>
    <svg width="360" height="620" style="position:absolute;left:0;top:0" aria-hidden="true">
      <polygon points="0,400 360,250 360,620 0,620" fill="#8a8b8f"/>
      <polygon points="270,0 360,0 360,620 250,620 360,250" fill="#c8202c"/>
      <polyline points="40,120 40,80 130,80" fill="none" stroke="#e0583a" stroke-width="5"/>
    </svg>
    <div class="photo rider-photo" role="img" aria-label="Photo of a rider on a trail bike on a forest mountain road"></div>
    <div class="sq-orange"></div>
    <div class="sq-navy"></div>
    <div class="web">www.ridgelinethrottle.co.uk</div>
  </div>

  <div class="panel contact-panel">
    <div class="photo texture" role="img" aria-label="Rocky mountain track photo with a red tint"></div>
    <div class="contact-panel__inner">
      <h3>Where to Find Us?</h3>
      <p class="body-text">With a base in the UK and a home in Nepal, we are always happy to talk routes, bikes and plans for your ride.</p>
      <div class="map" role="img" aria-label="Small map showing the location of the Kathmandu office"></div>
      <p class="body-text">If you are visiting, drop in for a chai and a chat about the road ahead.</p>
      <p class="lead">Looking forward to hearing from you! Mara</p>
      <p class="detail">Mobile/ WhatsApp: +44 0700 000 0000<br>Email: mara@ridgelinethrottle.co.uk</p>
      <p class="lead">Already in Kathmandu?</p>
      <p class="body-text">Come and find us in Thamel, just off the main square near the old temple.</p>
      <small>Please book at least four weeks ahead so we can sort permits, bikes and guides for you.</small>
    </div>
  </div>

  <div class="panel cover-panel">
    <div class="photo mountain-photo" role="img" aria-label="Photo of a rider with arms raised beside a motorcycle below snowy Himalayan peaks"></div>
    <div class="brand"><span class="brand__dot"></span>Ridgeline Throttle</div>
    <svg width="360" height="620" style="position:absolute;left:0;top:0" aria-hidden="true">
      <polygon points="0,380 360,330 360,620 0,620" fill="#f4f4f6"/>
      <g stroke="#d6d6da" stroke-width="1">
        <line x1="0" y1="440" x2="360" y2="400"/><line x1="0" y1="460" x2="360" y2="420"/>
        <line x1="0" y1="480" x2="360" y2="440"/><line x1="0" y1="500" x2="360" y2="460"/>
        <line x1="0" y1="520" x2="360" y2="480"/>
      </g>
      <polyline points="40,560 110,400 130,400" fill="none" stroke="#e0583a" stroke-width="8"/>
      <polyline points="330,20 360,20" fill="none" stroke="#e0583a" stroke-width="8"/>
    </svg>
    <h1 class="cover-panel__title">The Ultimate Himalayan Motorcycle Adventure</h1>
    <div class="cover-panel__url web">www.ridgelinethrottle.co.uk</div>
  </div>
</section>

<!-- Inside spread: about, social work, touring -->
<section class="spread spread--inside">
  <div class="panel about-page">
    <div class="photo road-photo" role="img" aria-label="Mountain road photo under a deep red overlay"></div>
    <div class="about-page__col about-page__col--a">
      <h2 class="heading heading--light">About Us</h2>
      <div class="body-text">
        <p>Here at Ridgeline Throttle we are the creators and the providers of all our motorcycle tours.</p>
        <p>With years of riding these roads, we know every pass, village and tea stop between the plains and the high Himalaya, and we love to share them.</p>
        <p>We have a fleet of well kept Kestrel trail bikes, serviced by our own mechanics and ready for rough mountain tracks.</p>
        <p>Anyone is welcome to sign up to one of our Himalayan adventures, no matter what gender, age, ethnicity or belief.</p>
      </div>
      <h2 class="heading heading--light">Social Work</h2>
      <div class="body-text">
        <p>Each trip we run helps fund local projects in Nepal. We give to a school fund in the hills, supporting students from low income families with books, uniforms and fees. It is one of the best ways to give young people a chance at further education.</p>
      </div>
    </div>
    <div class="about-page__col about-page__col--b">
      <h2 class="heading heading--light">Social Work</h2>
      <div class="body-text">
        <p>Since our first season we have worked with villages along our routes, helping repair trails, classrooms and water taps. Riders often join in for a morning, and many say it is the part of the trip they remember most.</p>
        <p>Every ride also supports the families who work beside us, from cooks and drivers to local guides who know each valley by heart.</p>
        <p>Our mechanics train young people from the hills, giving them a trade they can carry anywhere. Ask us how your tour helps, and we will happily show you the projects on the way.</p>
      </div>
    </div>
  </div>

  <div class="panel touring-page">
    <div class="touring-page__inner">
      <h2 class="heading heading--navy">Touring in the HIMALAYAS</h2>
      <div class="body-text">
        <p>Nepal is a country that stretches from the plains of the south to the roof of the world. Within a short ride you pass rice terraces, pine forests, river gorges and high desert, with the greatest peaks on earth watching over every bend. Few places give a rider so much change in a single day.</p>
        <p>Our routes follow old trade roads and new mountain tracks, linking villages, monasteries and hill towns where travellers are welcomed with warm food and open doors. Each tour is planned so you ride hard by day and rest well by night, with time to stop, look and talk.</p>
        <p>Tiny villages cling to ridges across the country, each with its own festivals, crafts and stories. Riding here is less about speed and more about the journey, the people you meet and the mountains that make it all possible for the adventurous traveller.</p>
      </div>
    </div>
    <svg class="page-band" viewBox="0 0 540 26" preserveAspectRatio="none" aria-hidden="true">
      <polygon points="0,26 0,12 540,0 540,26" fill="#2b2f86"/>
      <polygon points="0,12 540,0 540,4 0,16" fill="#c8202c"/>
    </svg>
  </div>
</section>

<!-- Services spread: story and our services -->
<section class="spread spread--services">
  <div class="panel story-page">
    <div class="photo valley-photo" role="img" aria-label="Faint valley landscape photo under a navy overlay"></div>
    <div class="story-page__col story-page__col--a body-text">
      <p>Every tour begins in Kathmandu, where we fit your bike, check your kit and share a meal before the road. From there we climb out of the valley towards the hills, riding through farms and forests before the first big passes come into view.</p>
      <p>Our guides ride with you the whole way, and a support vehicle carries luggage, spares and fuel, so you can focus on the riding. Evenings are spent in family lodges with hot food and good company.</p>
      <p>Routes are graded so both new and seasoned riders find the right challenge.</p>
    </div>
    <div class="story-page__col story-page__col--b body-text">
      <p>Higher up, the roads turn to gravel and rock, crossing rivers and winding past prayer walls and small gompas. The air is thin, the views are huge and every summit feels earned.</p>
      <p>We keep groups small so the trip stays personal, and we are flexible when weather or curiosity calls for a change of plan. Rest days let you explore on foot or simply sit and watch the mountains.</p>
      <p>By the end, most riders leave with new friends, a dusty bike and a promise to return for another season.</p>
    </div>
    <svg width="540" height="620" style="position:absolute;left:0;top:0" aria-hidden="true">
      <polygon points="0,560 540,590 540,620 0,620" fill="#1d2060"/>
      <polygon points="0,548 540,578 540,584 0,556" fill="#c8202c"/>
    </svg>
  </div>

  <div class="panel services-page">
    <div class="services-page__inner">
      <h2 class="heading heading--navy">Our Services</h2>
      <ul class="services-list">
        <li><strong>Guided Motorcycle Tours</strong> around Nepal and Tibet</li>
        <li><strong>Day Rides</strong> around the Kathmandu Valley</li>
        <li><strong>Bespoke Trips</strong>, trekking, mountain biking, white water rafting and more</li>
        <li><strong>Heli Taxis</strong>, for those short on time to reach popular trekking routes</li>
        <li><strong>Photo Tours</strong>, plus photography, art and writing retreats</li>
      </ul>
      <p class="partner">All organised with</p>
      <div class="partner-badge" role="img" aria-label="Travel partner badge"></div>
    </div>
    <svg class="collage" width="540" height="620" style="left:0;top:0" aria-hidden="true">
      <polygon points="540,330 540,620 380,620" fill="#2a2a2e"/>
      <polygon points="0,560 540,600 540,620 0,620" fill="#2b2f86"/>
      <polygon points="0,548 540,588 540,594 0,554" fill="#c8202c"/>
      <rect x="230" y="380" width="60" height="60" fill="#f0c9c2"/>
      <rect x="250" y="470" width="40" height="40" fill="#2b2f86"/>
      <rect x="360" y="520" width="46" height="46" fill="#2b2f86"/>
    </svg>
    <div class="photo" role="img" aria-label="Photo of a colourful Nepali temple deity mask" style="left:350px;top:360px;width:130px;height:140px;background:linear-gradient(150deg,#c8202c,#e6a23a 50%,#2b2f86)"></div>
    <div class="photo" role="img" aria-label="Photo of prayer wheels and temple detail" style="left:290px;top:420px;width:70px;height:90px;background:linear-gradient(160deg,#b37a3c,#6a3b1e)"></div>
    <div class="photo" role="img" aria-label="Photo of a rider on a mountain road" style="left:420px;top:300px;width:80px;height:70px;background:linear-gradient(170deg,#9fb0c4,#5b5246)"></div>
  </div>
</section>

</body>
</html>
```